Design a Restaurant Menu for Modern Japanese Restaurant

Please design a Restaurant Menu for Modern Japanese Restaurant.
Following is the sample menu design.
No need to be similar with sample design, but prefer with this layout
(of cause you can change around the layout)
First page
https://www.quillvault.com/s/mr7pk2zqe55wbnj/top_menu_first_page.pdf?dl=0
Secand and Third page
https://www.quillvault.com/s/hgs3ruyw82cfq0t/Secand_and%20Third_page.doc?dl=0
Last page
https://www.quillvault.com/s/wzt6mlpa19xjkrb/Last_page.doc?dl=0
total 4 pages with A4 size. (like a 2 page book)
design taste: Simple, conspicuous, easy viewing.
you can use any photo from the following link and website.
photo link
https://www.quillvault.com/sh/k42mnbzrtqu8e/BBHTQrvLmPgWsaYuDeNhT47kd?dl=0
Website
http://tallowreedkitchen.com.au/4/TALLOW_REED_KITCHEN-TOP.html

```html
<!DOCTYPE html>
<html lang="en">
<head>
<meta charset="utf-8">
<title>Tallow Reed Kitchen — Menu</title>
<link href="https://fonts.googleapis.com/css2?family=Raleway:wght@300;400&family=Lobster&family=Oswald:wght@300;400;500&family=Courgette&display=swap" rel="stylesheet">
<style>
  :root{
    --backdrop-top:#f4ece6;
    --backdrop-bottom:#e6d8cf;
    --cover-dark:#1c130e;
    --cover-warm:#6b4a33;
    --cover-glow:#a67d5a;
    --page-light:#f2f2f2;
    --page-shade:#c9c9c9;
    --ink:#2b2b2b;
    --ink-soft:#5c5c5c;
    --ribbon:#d23a3a;
    --ribbon-dark:#a82828;
    --white:#ffffff;
    --logo-box:#8d8a86;
  }
  *{box-sizing:border-box;margin:0;padding:0}
  html,body{width:1200px;height:687px;overflow:hidden}
  body{background:linear-gradient(180deg,var(--backdrop-top),var(--backdrop-bottom));font-family:'Oswald',sans-serif;position:relative}

  .cover{position:absolute;left:170px;top:100px;width:300px;height:470px;background:var(--cover-dark);border:8px solid #0d0907;box-shadow:0 14px 30px rgba(0,0,0,.35);overflow:hidden}
  .cover-photo{position:absolute;inset:0;background:radial-gradient(ellipse at 40% 55%,var(--cover-glow) 0%,var(--cover-warm) 35%,var(--cover-dark) 80%)}
  .cover-title{position:absolute;top:22px;left:0;right:0;text-align:center;color:var(--white);font-family:'Raleway',sans-serif;font-weight:300;font-size:52px;letter-spacing:6px}
  .cover-subtitle{position:absolute;top:92px;left:0;right:0;text-align:center;color:var(--white);font-family:'Courgette',cursive;font-size:19px;line-height:1.35}
  .cover-brand{position:absolute;left:20px;bottom:20px;width:78px;height:78px;background:var(--logo-box);display:flex;align-items:flex-end;justify-content:center;padding:0 4px 8px}
  .cover-brand span{color:var(--white);font-family:'Raleway',sans-serif;font-size:8px;font-weight:400;text-align:center;line-height:1.2}

  .sheet{position:absolute;left:510px;top:100px;width:360px;height:470px;box-shadow:0 14px 30px rgba(0,0,0,.3);overflow:hidden}
  .sheet-photo{position:absolute;inset:0;background:linear-gradient(135deg,var(--page-light) 0%,#e4e4e4 55%,var(--page-shade) 100%)}
  .sheet-divider{position:absolute;left:180px;top:20px;bottom:20px;width:1px;background:var(--ribbon)}
  .column{position:absolute;top:0;width:180px;padding:0 14px}
  .column.left{left:0}
  .column.right{left:180px}
  .ribbon{display:inline-block;background:var(--ribbon);color:var(--white);font-family:'Lobster',cursive;font-size:17px;font-weight:400;padding:3px 14px 4px;box-shadow:2px 2px 0 var(--ribbon-dark);margin:0 0 10px}
  .column.left .ribbon{margin-left:-14px}
  .item{display:flex;justify-content:space-between;gap:6px;margin-bottom:9px}
  .item-name{font-size:8px;font-weight:500;text-transform:uppercase;color:var(--ink);letter-spacing:.3px;line-height:1.3}
  .item-desc{display:block;font-weight:300;font-size:7px;text-transform:none;color:var(--ink-soft);margin-top:1px;line-height:1.35}
  .item-price{font-size:8px;color:var(--ink);white-space:nowrap}
</style>
</head>
<body>

<section class="cover">
  <div class="cover-photo" role="img" aria-label="Dimly lit restaurant dining table with candle and wine glasses"></div>
  <h1 class="cover-title">MENU</h1>
  <p class="cover-subtitle">Contemporary<br>Australian | Japanese</p>
  <div class="cover-brand"><span>Tallow Reed Kitchen</span></div>
</section>

<section class="sheet">
  <div class="sheet-photo" role="img" aria-label="Faded restaurant interior photograph behind the menu"></div>
  <div class="sheet-divider"></div>

  <div class="column left">
    <h2 class="ribbon" style="margin-top:18px">Sides</h2>
    <div class="item"><span class="item-name">Miso soup w/ mushrooms</span><span class="item-price">3.00</span></div>
    <div class="item"><span class="item-name">Steamed rice w/ quinoa</span><span class="item-price">3.00</span></div>
    <div class="item"><span class="item-name">Green salad w/ sesame dressing</span><span class="item-price">5.50</span></div>
    <div class="item"><span class="item-name">Soft shell crab w/ wasabi caviar cream</span><span class="item-price">10.00</span></div>

    <h2 class="ribbon" style="margin-top:10px">Desserts</h2>
    <div class="item"><span class="item-name">Matcha brulee<span class="item-desc">lightly torched green tea custard brulee</span></span><span class="item-price">6.50</span></div>
    <div class="item"><span class="item-name">Espresso pannacotta<span class="item-desc">espresso pannacotta, coffee jelly</span></span><span class="item-price">6.50</span></div>
    <div class="item"><span class="item-name">Blood orange &amp; coconut gelato<span class="item-desc">blood orange sorbet, coconut gelato, crushed nuts &amp; cookies</span></span><span class="item-price">6.50</span></div>
    <div class="item"><span class="item-name">Banana azuki &amp; chocolate roll<span class="item-desc">with fresh banana &amp; chocolate, blood orange &amp; coconut</span></span><span class="item-price">11.00</span></div>
  </div>

  <div class="column right">
    <h2 class="ribbon" style="margin-top:30px;margin-left:20px">Beverages</h2>
    <div class="item"><span class="item-name">Coffees<span class="item-desc">flat white · latte · cappuccino<br>espresso · long black · macchiato<br>iced macchiato · affogato (+2.00)</span></span><span class="item-price">4.00</span></div>
    <div class="item"><span class="item-name">Teas<span class="item-desc">chai · english breakfast<br>earl grey · jasmine green · peppermint<br>rooibos (vanilla flavour)</span></span><span class="item-price">4.00</span></div>
    <div class="item"><span class="item-name">Genmai Japanese tea</span><span class="item-price">4.00</span></div>
    <div class="item"><span class="item-name">Mineral water<span class="item-desc">sparkling / still (1L)</span></span><span class="item-price">6.50</span></div>
    <div class="item"><span class="item-name">Flavoured natural water<span class="item-desc">zesty lemon · crisp apple<br>wild raspberry</span></span><span class="item-price">6.50</span></div>
    <div class="item"><span class="item-name">Soft drinks<span class="item-desc">cola · diet cola · lemon lime &amp; bitter</span></span><span class="item-price">3.50</span></div>
    <div class="item"><span class="item-name">Orange juice</span><span class="item-price">4.50</span></div>
  </div>
</section>

</body>
</html>
```